Letterhead

Can you please design me a letterhead that I can use electronically in word as a template. I have attached my business card as I would like the design to reflect this logo.

```html
<!DOCTYPE html>
<html lang="en">
<head>
<meta charset="utf-8">
<title>Talvenco Letterhead</title>
<link href="https://fonts.googleapis.com/css2?family=Open+Sans:wght@400;700&family=Arimo:wght@400&display=swap" rel="stylesheet">
<style>
  :root {
    --brand-red: #bc1e24;
    --ink-grey: #3d3d3f;
    --paper: #ffffff;
    --pattern-tint: #f6d3d5;
  }
  html, body {
    margin: 0;
    padding: 0;
    overflow: hidden;
    background: var(--paper);
  }
  .letterhead {
    position: relative;
    width: 843px;
    height: 1200px;
    background: var(--paper);
    overflow: hidden;
  }
  .side-band {
    position: absolute;
    left: 0;
    top: 0;
    width: 14px;
    height: 100%;
    background: var(--brand-red);
  }
  .contact-block {
    position: absolute;
    left: 43px;
    top: 21px;
    font-family: "Open Sans", sans-serif;
    color: var(--ink-grey);
  }
  .contact-name {
    font-size: 12.5px;
    font-weight: 700;
    line-height: 16px;
  }
  .contact-role {
    font-weight: 400;
    font-size: 11px;
    color: var(--brand-red);
  }
  .divider {
    display: inline-block;
    width: 2px;
    height: 11px;
    background: var(--brand-red);
    margin: 0 5px;
    vertical-align: -1px;
  }
  .contact-details {
    font-size: 10px;
    line-height: 15px;
  }
  .label {
    color: var(--brand-red);
  }
  .brand {
    position: absolute;
    left: 419px;
    top: 34px;
    font-family: "Arimo", sans-serif;
    color: var(--brand-red);
  }
  .brand-name {
    font-size: 76px;
    line-height: 84px;
    font-weight: 400;
    letter-spacing: 1px;
  }
  .brand-tagline {
    margin-top: 9px;
    font-size: 16.5px;
    color: #1d1d1d;
  }
  .pattern-top {
    position: absolute;
    right: 0;
    top: 0;
    width: 220px;
    height: 198px;
    background: radial-gradient(ellipse at 100% 30%, var(--pattern-tint) 0%, rgba(246,211,213,0.55) 45%, rgba(255,255,255,0) 75%);
  }
  .pattern-bottom {
    position: absolute;
    right: 0;
    bottom: 0;
    width: 120px;
    height: 112px;
    background: radial-gradient(ellipse at 100% 100%, var(--pattern-tint) 0%, rgba(246,211,213,0.5) 45%, rgba(255,255,255,0) 78%);
  }
</style>
</head>
<body>
  <main class="letterhead">
    <div class="side-band"></div>

    <div class="pattern-top" role="img" aria-label="Decorative pattern of outlined red cubes fanning from the top right corner"></div>
    <div class="pattern-bottom" role="img" aria-label="Decorative pattern of outlined red cubes in the bottom right corner"></div>

    <header class="contact-block">
      <div class="contact-name">Miriam Calloway<span class="divider"></span><span class="contact-role">Principal</span></div>
      <div class="contact-details">
        <span class="label">P</span> : 0400 555 018<span class="divider"></span><span class="label">E</span> : miriam@talvenco.net.au<span class="divider"></span><span class="label">ACN</span> : 012 345 678
      </div>
    </header>

    <div class="brand">
      <div class="brand-name">talvenco</div>
      <div class="brand-tagline">Business Consultants Pty Ltd</div>
    </div>
  </main>
</body>
</html>
```